Fresh and unique Mortgage Broking business needs website design.

We need a professional yet fresh, bright and colourful website for my Mortgage broking business.
We specialise in the Non conforming/sub prime market with clients who have been rejected by other banks or have trouble getting finance through a traditional lender.
We are called Lark Lending and we aim to provide Hope to our clients when they have thought there was no hope.
I would like it to be on a Wordpress platform as I plan to do a lot of postings, both written and video and I need it to be easy to use.
I would also like it to be able to have a clear and simple enquiry box on the first page to capture contact details and notify me via email.

I have already had the logo designed in both green and black and a white version.
I have also had a a header made up using the white logo with leaves background that could possibly be used as the website header which I have used as my facebook header.

https://www.facebook.com/MarcusWendellLark/

I tried playing around with a jimdo website builder which kind of got some of the brightness and colours I was after but it had a lot to go.

http://larklending.sitebuildr.example/

Colors
0292cd
00a990
fbed22
ffc214
f78f20
ec1f27

• I'm not sure what the difference between uncoded and coded website is so I'm not sure what I need?

```html
<!DOCTYPE html>
<html lang="en">
<head>
<meta charset="utf-8">
<title>Lark Lending</title>
<link href="https://fonts.googleapis.com/css2?family=Lora:ital,wght@0,400;0,700;1,400&family=Open+Sans:ital,wght@0,400;0,600;0,700;1,400&display=swap" rel="stylesheet">
<style>
:root{
  --orange:#f78f20;
  --teal:#00a990;
  --blue:#0292cd;
  --yellow:#ffc214;
  --red:#ec1f27;
  --green:#1e7a3c;
  --ink:#222;
  --text:#555;
  --muted:#888;
  --line:#ddd;
  --band:#eef1f3;
}
*{box-sizing:border-box;margin:0;padding:0}
html,body{width:1200px;height:2359px;overflow:hidden;background:#fff}
body{position:relative;font-family:"Open Sans",Arial,sans-serif;color:var(--text)}
.abs{position:absolute}
.serif{font-family:"Lora",Georgia,serif}

/* header */
.site-header{position:absolute;left:0;top:0;width:1200px;height:96px}
.brand{position:absolute;left:99px;top:22px;display:flex;align-items:center;gap:10px;font-family:"Lora",Georgia,serif;font-weight:700;font-size:34px;color:var(--green)}
.brand .dot{width:14px;height:14px;border-radius:50%;background:var(--green)}
.top-contact{position:absolute;right:98px;top:12px;display:flex;gap:26px;font-family:"Lora",serif;font-size:16px;color:var(--ink)}
.top-contact span{display:flex;align-items:center;gap:12px}
.ring{width:36px;height:36px;border:1px solid #ccc;border-radius:50%;display:flex;align-items:center;justify-content:center}
.main-nav{position:absolute;right:98px;top:64px;display:flex;gap:40px;font-family:"Lora",serif;font-size:14px;color:var(--ink);align-items:center}
.main-nav .active{color:var(--orange)}

/* hero */
.hero{position:absolute;left:0;top:96px;width:1200px;height:464px;
  background:radial-gradient(ellipse at 70% 30%,#e2661a 0%,#b8400e 25%,transparent 55%),
  radial-gradient(ellipse at 20% 60%,#c9a030 0%,#8a7a25 35%,transparent 70%),
  linear-gradient(100deg,#c46b1a 0%,#a55616 45%,#6b1a0a 75%,#1a0604 100%)}
.hero h1{position:absolute;left:97px;top:158px;font-family:"Lora",serif;font-weight:700;font-size:50px;color:#fff;letter-spacing:1px}
.hero p{position:absolute;left:97px;top:232px;width:600px;font-size:18px;line-height:31px;font-weight:600;color:#fff}
.btn-ghost{position:absolute;left:97px;top:343px;width:161px;height:39px;border:1px solid #fff;border-radius:4px;color:#fff;font-weight:700;font-size:15px;display:flex;align-items:center;justify-content:center;letter-spacing:.5px}
.slider-dots{position:absolute;left:535px;top:412px;display:flex;gap:5px}
.slider-dots i{width:30px;height:5px;border-radius:3px;border:1px solid #fff}
.slider-dots i.on{background:#fff}

/* about */
.about h2{position:absolute;left:97px;top:612px;width:480px;font-family:"Lora",serif;font-weight:700;font-size:24px;line-height:35px;color:var(--ink)}
.about p{position:absolute;left:97px;width:500px;font-size:12.5px;line-height:21px;color:var(--text)}
.btn-line{position:absolute;height:35px;border:1px solid #bbb;color:var(--orange);font-weight:700;font-size:12.5px;display:flex;align-items:center;justify-content:center}
.video-frame{position:absolute;left:637px;top:613px;width:465px;height:277px;border:1px solid #ddd;padding:4px;background:#fff;box-shadow:0 1px 3px rgba(0,0,0,.15)}
.video-frame .media{width:100%;height:100%;background:linear-gradient(160deg,#8fae6a 0%,#c7d2b8 40%,#e9e1d3 60%,#6f9a45 100%);position:relative}
.play{position:absolute;left:50%;top:50%;width:56px;height:56px;margin:-28px 0 0 -28px;border-radius:50%;background:rgba(0,0,0,.55);border:2px solid #fff}

/* services */
.services{position:absolute;left:0;top:945px;width:1200px;height:404px;background:var(--band)}
.section-title{font-family:"Lora",serif;font-weight:700;font-size:25px;color:var(--ink)}
.services .section-title{position:absolute;left:0;width:1200px;top:45px;text-align:center}
.service{position:absolute;width:320px}
.service svg{position:absolute;left:0;top:0}
.service h3{position:absolute;left:70px;top:0;font-family:"Lora",serif;font-weight:700;font-size:18px;color:var(--ink);white-space:nowrap}
.service p{position:absolute;left:70px;top:33px;width:235px;font-size:12px;line-height:22px;color:var(--text)}

/* why + blog */
.why .section-title,.blog .section-title{position:absolute;top:1400px}
.why-intro{position:absolute;left:97px;top:1452px;width:450px;font-size:12px;line-height:21px}
.ticks{position:absolute;left:97px;top:1518px;list-style:none}
.ticks li{height:38.5px;display:flex;gap:16px;font-size:12px;align-items:flex-start}
.ticks li svg{flex:none;margin-top:1px}
.more{position:absolute;color:var(--orange);font-weight:700;font-size:12.5px}
.post{position:absolute;left:587px;width:515px;height:155px;border-bottom:1px solid var(--line)}
.post .thumb{position:absolute;left:0;top:0;width:155px;height:120px;border:1px solid #ddd;padding:4px;background:#fff;box-shadow:0 1px 3px rgba(0,0,0,.12)}
.post .thumb div{width:100%;height:100%}
.post h4{position:absolute;left:176px;top:0;width:340px;font-size:14px;line-height:23px;font-weight:700;color:var(--ink);text-decoration:underline}
.post .meta{position:absolute;left:176px;top:52px;font-size:11.5px;color:var(--muted);font-style:italic;display:flex;gap:16px}
.post p{position:absolute;left:176px;top:76px;width:340px;font-size:12px;line-height:22px}

/* testimonial */
.testimonial{position:absolute;left:0;top:1835px;width:1200px;height:210px;background:var(--teal)}
.avatar{position:absolute;left:110px;top:40px;width:126px;height:126px;border-radius:50%;border:4px solid #fff;background:linear-gradient(180deg,#d8d3cc,#9aa3ab)}
.testimonial .rule{position:absolute;left:270px;top:40px;width:1px;height:128px;background:rgba(255,255,255,.6)}
.testimonial blockquote{position:absolute;left:303px;top:44px;width:820px;font-style:italic;font-size:15px;line-height:26px;color:#fff}
.testimonial cite{position:absolute;left:303px;top:142px;font-family:"Lora",serif;font-weight:700;font-style:normal;font-size:18px;color:#fff}

/* footer */
.footer-brand{position:absolute;left:99px;top:2150px;display:flex;align-items:center;gap:12px;font-family:"Lora",serif;font-weight:700;font-size:42px;color:var(--green)}
.footer-brand .dot{width:18px;height:18px;border-radius:50%;background:var(--green)}
.fcol h5{position:absolute;top:2094px;font-family:"Lora",serif;font-weight:700;font-size:16px;color:var(--ink)}
.flinks{position:absolute;left:426px;top:2130px;list-style:none;font-size:12px;line-height:29px;color:var(--ink)}
.news-copy{position:absolute;left:594px;top:2132px;width:230px;font-size:12px;line-height:20px;color:var(--ink)}
.email-field{position:absolute;left:594px;top:2180px;width:254px;height:35px;background:#f0f0f0;font-size:11.5px;color:#aaa;padding:10px 14px}
.contact-list{position:absolute;left:900px;top:2130px;list-style:none;font-size:12px;color:var(--ink)}
.contact-list li{height:36.5px;display:flex;gap:18px;align-items:flex-start}
.contact-list svg{flex:none}
.footer-rule{position:absolute;left:97px;top:2295px;width:1005px;height:1px;background:var(--line)}
.copyright{position:absolute;left:97px;top:2318px;font-size:12px;color:var(--ink)}
.social{position:absolute;left:978px;top:2313px;display:flex;gap:8px}
.social i{width:25px;height:25px;border-radius:50%;border:1px solid var(--orange)}
</style>
</head>
<body>

<header class="site-header">
  <div class="brand"><span class="dot"></span>Lark Lending</div>
  <div class="top-contact">
    <span><span class="ring"><svg width="14" height="14" viewBox="0 0 24 24"><path fill="#f78f20" d="M6.6 10.8a15 15 0 0 0 6.6 6.6l2.2-2.2c.3-.3.7-.4 1-.2 1.1.4 2.3.6 3.6.6.6 0 1 .4 1 1V20c0 .6-.4 1-1 1A17 17 0 0 1 3 4c0-.6.4-1 1-1h3.5c.6 0 1 .4 1 1 0 1.3.2 2.5.6 3.6.1.3 0 .7-.2 1z"/></svg></span>0491 570 156</span>
    <span><span class="ring"><svg width="15" height="12" viewBox="0 0 24 18"><path fill="#f78f20" d="M0 0h24v3L12 10 0 3zM0 5l12 7 12-7v13H0z"/></svg></span>Marcus@larklending.example</span>
  </div>
  <nav class="main-nav">
    <span class="active">HOME</span><span>ABOUT</span><span>SERVICES</span><span>PROPERTY ADVICE</span><span>CONTACT</span>
    <svg width="13" height="13" viewBox="0 0 24 24"><circle cx="10" cy="10" r="7" fill="none" stroke="#222" stroke-width="3"/><path d="M15 15l7 7" stroke="#222" stroke-width="3"/></svg>
  </nav>
</header>

<section class="hero" role="img" aria-label="Autumn maple leaves in orange and red against a soft green background">
  <h1>LARK LENDING</h1>
  <p>We specialise in the Non conforming/sub prime market with clients who have been rejected by other banks or have trouble getting finance through a traditional lender.</p>
  <div class="btn-ghost">GET A QUOTE</div>
  <div class="slider-dots"><i class="on"></i><i></i><i></i><i></i></div>
</section>

<section class="about">
  <h2>HOPE FOR YOUR FINANCE WHEN ALL HOPE IS LOST</h2>
  <p style="top:693px">Lark Lending is a Christian Mortgage Broking business. Marcus lives in Brookvale and loves exploring the Westmere Shire with his wife and kids for great places to eat.</p>
  <p style="top:756px">With over 10 years' experience in financial services ranging from insurance, superannuation, investments and finance, Marcus bringing together his experience to provide a more holistic approach to his customers.</p>
  <div class="btn-line" style="left:97px;top:849px;width:129px">READ MORE &gt;&gt;</div>
  <div class="video-frame"><div class="media" role="img" aria-label="Video still of a smiling family outside their home"><span class="play"><svg width="52" height="52" viewBox="0 0 52 52"><path d="M21 16l16 10-16 10z" fill="#fff"/></svg></span></div></div>
</section>

<section class="services">
  <h2 class="section-title">OUR SERVICES</h2>
  <div class="service" style="left:97px;top:117px">
    <svg width="46" height="40" viewBox="0 0 46 40"><path d="M23 2L2 20h6v18h11V27h8v11h11V20h6z" fill="var(--blue)"/></svg>
    <h3>Residential loans</h3><p>At vero eos et accusamus et iust odio dignissimos ducimus qui blanditiis pr aesentium voluptat.</p>
  </div>
  <div class="service" style="left:459px;top:117px">
    <svg width="56" height="44" viewBox="0 0 56 44"><path d="M2 2v40h52" fill="none" stroke="var(--yellow)" stroke-width="3"/><rect x="10" y="22" width="6" height="16" fill="var(--yellow)"/><rect x="20" y="14" width="6" height="24" fill="var(--yellow)"/><rect x="30" y="18" width="6" height="20" fill="var(--yellow)"/><rect x="40" y="8" width="6" height="30" fill="var(--yellow)"/></svg>
    <h3>Investment loans</h3><p>At vero eos et accusamus et iust odio dignissimos ducimus qui blanditiis pr aesentium voluptat.</p>
  </div>
  <div class="service" style="left:822px;top:117px">
    <svg width="42" height="44" viewBox="0 0 42 44"><circle cx="21" cy="12" r="11" fill="var(--teal)"/><path d="M1 44c0-12 9-19 20-19s20 7 20 19z" fill="var(--teal)"/></svg>
    <h3>Self employed loans</h3><p>At vero eos et accusamus et iust odio dignissimos ducimus qui blanditiis pr aesentium voluptat.</p>
  </div>
  <div class="service" style="left:97px;top:250px">
    <svg width="50" height="46" viewBox="0 0 50 46"><path d="M25 2L48 44H2z" fill="var(--red)"/><rect x="22.5" y="15" width="5" height="17" fill="#fff"/><rect x="22.5" y="35" width="5" height="5" fill="#fff"/></svg>
    <h3>Non confirming loans</h3><p>At vero eos et accusamus et iust odio dignissimos ducimus qui blanditiis pr aesentium voluptat.</p>
  </div>
  <div class="service" style="left:459px;top:250px">
    <svg width="46" height="46" viewBox="0 0 46 46"><rect x="2" y="2" width="9" height="24" fill="var(--green)"/><path d="M14 2h20c3 0 5 2 5 5l3 17c0 3-2 5-5 5H28l2 10c0 3-2 5-4 5l-12-17z" fill="var(--green)"/></svg>
    <h3>Bad credit &amp; Low doc</h3><p>At vero eos et accusamus et iust odio dignissimos ducimus qui blanditiis pr aesentium voluptat.</p>
  </div>
  <div class="service" style="left:822px;top:250px">
    <svg width="54" height="42" viewBox="0 0 54 42"><rect x="2" y="2" width="50" height="38" rx="4" fill="none" stroke="var(--orange)" stroke-width="3"/><rect x="2" y="11" width="50" height="7" fill="var(--orange)"/><rect x="8" y="28" width="14" height="4" fill="var(--orange)"/></svg>
    <h3>Debt consolidation</h3><p>At vero eos et accusamus et iust odio dignissimos ducimus qui blanditiis pr aesentium voluptat.</p>
  </div>
</section>

<section class="why">
  <h2 class="section-title" style="left:97px">WHY CHOOSE US</h2>
  <p class="why-intro">At vero eos et accusamus et iusto odio dignissimos ducimus qui blanditii praese ntium voluptatum deleniti atque corrupti quos .</p>
  <ul class="ticks">
    <li><svg width="15" height="15" viewBox="0 0 16 16"><circle cx="8" cy="8" r="8" fill="var(--teal)"/><path d="M4 8l3 3 5-6" fill="none" stroke="#fff" stroke-width="2"/></svg>Blanditiis praesentium voluptatum deleniti atque corrupti quos</li>
    <li><svg width="15" height="15" viewBox="0 0 16 16"><circle cx="8" cy="8" r="8" fill="var(--teal)"/><path d="M4 8l3 3 5-6" fill="none" stroke="#fff" stroke-width="2"/></svg>Sed ut perspiciatis unde omnis iste natus error sit voluptatem accusanti</li>
    <li><svg width="15" height="15" viewBox="0 0 16 16"><circle cx="8" cy="8" r="8" fill="var(--teal)"/><path d="M4 8l3 3 5-6" fill="none" stroke="#fff" stroke-width="2"/></svg>But I must explain to you how all this mistaken idea of denouncing</li>
    <li><svg width="15" height="15" viewBox="0 0 16 16"><circle cx="8" cy="8" r="8" fill="var(--teal)"/><path d="M4 8l3 3 5-6" fill="none" stroke="#fff" stroke-width="2"/></svg>Nemo enim ipsam voluptatem quia voluptas sit aspernatur</li>
    <li><svg width="15" height="15" viewBox="0 0 16 16"><circle cx="8" cy="8" r="8" fill="var(--teal)"/><path d="M4 8l3 3 5-6" fill="none" stroke="#fff" stroke-width="2"/></svg>At vero eos et accusamus et iusto odio dignissimos ducimus qui</li>
    <li><svg width="15" height="15" viewBox="0 0 16 16"><circle cx="8" cy="8" r="8" fill="var(--teal)"/><path d="M4 8l3 3 5-6" fill="none" stroke="#fff" stroke-width="2"/></svg>Nam libero tempore, cum soluta nobis est eligendi optio cumque nihil</li>
  </ul>
  <span class="more" style="left:97px;top:1766px">READ MORE &gt;&gt;</span>
</section>

<section class="blog">
  <h2 class="section-title" style="left:588px">OUR BLOG</h2>
  <article class="post" style="top:1456px">
    <div class="thumb"><div role="img" aria-label="Happy couple at a beach" style="background:linear-gradient(135deg,#7fc8e8,#f2e6a0 60%,#d9c040)"></div></div>
    <h4>AT VERO EOS ET ACCUSAMUS ET IUSTO ODIODIG NISSIMOS DUCIMUS QUI BLAND</h4>
    <div class="meta"><span>15/10/2015</span><span>John Doe</span><span>4 Comments</span></div>
    <p>Duis aute irure dolor in reprehenderit in voluptate velit esse cillum dolore eu fugiat nulla pariatur.</p>
  </article>
  <article class="post" style="top:1612px">
    <div class="thumb"><div role="img" aria-label="Open hands holding a small house on grass" style="background:linear-gradient(180deg,#6fa8dc,#b9d6ee 55%,#e0b48a)"></div></div>
    <h4>AT VERO EOS ET ACCUSAMUS ET IUSTO ODIODIG NISSIMOS DUCIMUS QUI BLAND</h4>
    <div class="meta"><span>15/10/2015</span><span>John Doe</span><span>4 Comments</span></div>
    <p>Duis aute irure dolor in reprehenderit in voluptate velit esse cillum dolore eu fugiat nulla pariatur.</p>
  </article>
  <span class="more" style="left:588px;top:1766px">VIEW MORE &gt;&gt;</span>
</section>

<section class="testimonial">
  <svg class="abs" style="left:36px;top:92px" width="16" height="28" viewBox="0 0 16 28"><path d="M14 2L3 14l11 12" fill="none" stroke="#fff" stroke-width="2.5" opacity=".7"/></svg>
  <div class="avatar" role="img" aria-label="Portrait photo of the client giving the testimonial"></div>
  <div class="rule"></div>
  <blockquote>Nam libero tempore, cum soluta nobis est eligendi optio cumque nihil impedit quo minus id quod maxime placeat facere possimus, omnis voluptas assumenda est, omnis dolor repellendus. Temporibus autem quibusdam et aut officiis debitis aut rerum necessitatibus saepe eveniet ut et voluptates repudiandae sint et molestiae</blockquote>
  <cite>- Henri Dubreuil</cite>
  <svg class="abs" style="left:1146px;top:92px" width="16" height="28" viewBox="0 0 16 28"><path d="M2 2l11 12L2 26" fill="none" stroke="#fff" stroke-width="2.5" opacity=".7"/></svg>
</section>

<footer>
  <div class="footer-brand"><span class="dot"></span>Lark Lending</div>
  <div class="fcol">
    <h5 style="left:426px">Information</h5>
    <h5 style="left:594px">Newsletter Subscription</h5>
    <h5 style="left:900px">Contact Us</h5>
  </div>
  <ul class="flinks"><li>Home</li><li>About</li><li>Services</li><li>Property Advice</li><li>Contact</li></ul>
  <p class="news-copy">Register your Email Address to get information about us</p>
  <div class="email-field">Email Address</div>
  <div class="btn-line" style="left:594px;top:2232px;width:94px;height:30px;font-size:11.5px">SUBSCRIBE</div>
  <ul class="contact-list">
    <li><svg width="12" height="15" viewBox="0 0 12 16"><path d="M6 0a6 6 0 0 0-6 6c0 4.5 6 10 6 10s6-5.5 6-10a6 6 0 0 0-6-6zm0 8.5A2.5 2.5 0 1 1 6 3.5a2.5 2.5 0 0 1 0 5z" fill="var(--orange)"/></svg>Po Box 218 Brookvale VIC 3999</li>
    <li><svg width="13" height="13" viewBox="0 0 24 24"><path fill="var(--orange)" d="M6.6 10.8a15 15 0 0 0 6.6 6.6l2.2-2.2c.3-.3.7-.4 1-.2 1.1.4 2.3.6 3.6.6.6 0 1 .4 1 1V20c0 .6-.4 1-1 1A17 17 0 0 1 3 4c0-.6.4-1 1-1h3.5c.6 0 1 .4 1 1 0 1.3.2 2.5.6 3.6.1.3 0 .7-.2 1z"/></svg>0491 570 156</li>
    <li><svg width="14" height="14" viewBox="0 0 16 16"><rect x="1" y="5" width="14" height="10" fill="var(--orange)"/><rect x="4" y="1" width="8" height="5" fill="none" stroke="var(--orange)" stroke-width="1.5"/><rect x="4" y="8" width="8" height="4" fill="#fff"/></svg>(03) 5550 1234</li>
    <li><svg width="14" height="11" viewBox="0 0 24 18"><path fill="var(--orange)" d="M0 0h24v3L12 10 0 3zM0 5l12 7 12-7v13H0z"/></svg>Marcus@larklending.example</li>
  </ul>
  <div class="footer-rule"></div>
  <p class="copyright">Copyrights © 2016, Lark Lending. All rights reserved.</p>
  <div class="social"><i></i><i></i><i></i><i></i></div>
</footer>

</body>
</html>
```